A suite of 3-4 brand templates.

I would like various brand templates using my brand colours(see my logo) that I can add information to, so I can create different help guides/ infographics on various health and well being topics (anxiety, breathing techniques, pain relief, self hypnosis etc) that I can put on my website:-
www.brightpathwellnessgroup.com

I want to ability to add both text guides and other guides to be more visual.

Target Market(s)

Health and wellbeing clients (particularly people looking for hypnosis, pain reprocessing therapy, and health coaching.

Industry/Entity Type

Health and Psychology

Font styles to use
Sans Serif

Colors
0054AA
0677BA
7BADD7
CADEEF
E8F1F8
0094D4
00A9DD
6FCCEA
C7EBF8
E9F6FB
F0912C
F2A743
F7CA91
FBE8D2
FDF5EE

Requirements
Must have
• Brand colours, website and Logo
Nice to have
• To look visually appealing and professional.

```html
<!DOCTYPE html>
<html lang="en">
<head>
<meta charset="utf-8">
<title>Pain Reprocessing Therapy – Bright Path Wellness Group</title>
<link href="https://fonts.googleapis.com/css2?family=Poppins:wght@400;600;700&family=Roboto:wght@700;900&display=swap" rel="stylesheet">
<style>
  :root {
    --navy: #1f4e8c;
    --brand-blue: #0054aa;
    --sky: #0094d4;
    --orange: #f0912c;
    --amber: #f2a743;
    --ink: #1b1b1b;
    --line: #c9ced6;
    --paper: #ffffff;
    --mist: #e8f1f8;
    --peach: #fbe8d2;
  }
  * { margin: 0; padding: 0; box-sizing: border-box; }
  html, body { width: 1200px; height: 675px; overflow: hidden; background: var(--paper); }
  .page { position: relative; width: 1200px; height: 675px; font-family: "Poppins", sans-serif; color: var(--ink); }

  .site-nav { position: absolute; left: 0; top: 0; width: 1200px; height: 48px; background: var(--navy); }
  .site-nav a { position: absolute; top: 17px; color: #fff; text-decoration: none; font: 700 10.5px/1 "Poppins", sans-serif; letter-spacing: -0.2px; }
  .nav-home { left: 396px; } .nav-therapies { left: 454px; } .nav-approach { left: 545px; }
  .nav-resources { left: 649px; } .nav-contact { left: 735px; }
  .caret { display: inline-block; width: 5px; height: 5px; border-right: 1.6px solid #fff; border-bottom: 1.6px solid #fff; transform: rotate(45deg); margin: 0 0 2px 4px; }

  .brand { position: absolute; left: 104px; top: 104px; display: flex; align-items: center; gap: 7px; }
  .brand-dot { width: 22px; height: 22px; border-radius: 50%; background: var(--amber); }
  .brand-name { font: 700 13px/1.15 "Roboto", sans-serif; color: var(--brand-blue); width: 110px; }

  .illustration { position: absolute; left: 436px; top: 198px; width: 456px; height: 454px; border-radius: 8px;
    background: radial-gradient(ellipse at 55% 60%, var(--peach) 0%, var(--mist) 55%, #ffffff 100%); }

  .hero-kicker { position: absolute; left: 100px; top: 194px; font: 700 19px/1 "Roboto", sans-serif; color: var(--navy); white-space: nowrap; }
  .hero-kicker span { color: var(--amber); }
  .hero-title { position: absolute; left: 100px; top: 230px; font: 700 34px/36px "Roboto", sans-serif; color: var(--navy); letter-spacing: -0.3px; white-space: nowrap; }
  .hero-acronym { position: absolute; left: 99px; top: 302px; font: 900 52px/1 "Roboto", sans-serif; color: var(--amber); }

  .section-title { position: absolute; left: 100px; top: 444px; font: 700 27px/1 "Poppins", sans-serif; color: var(--navy); letter-spacing: -0.3px; }
  .intro-text { position: absolute; left: 101px; top: 506px; width: 206px; font: 400 11.1px/14.7px "Poppins", sans-serif; }

  .connectors { position: absolute; left: 0; top: 0; }

  .audience-heading { position: absolute; left: 913px; top: 161px; font: 700 17px/1 "Poppins", sans-serif; color: var(--navy); }
  .audience-heading strong { display: block; font-size: 26px; color: var(--amber); margin-top: 1px; }

  .audience-item { position: absolute; left: 913px; width: 240px; display: flex; gap: 17px; }
  .audience-icon { flex: 0 0 38px; height: 38px; border-radius: 50%; background: var(--amber); display: flex; align-items: center; justify-content: center; margin-top: -2px; }
  .audience-copy { width: 170px; }
  .audience-copy h3 { font: 700 11.6px/14.6px "Poppins", sans-serif; color: var(--navy); }
  .audience-copy p { font: 400 10.4px/14.6px "Poppins", sans-serif; }
  .item-back { top: 225px; } .item-fibro { top: 331px; } .item-headache { top: 437px; } .item-ibs { top: 528px; }
</style>
</head>
<body>
<div class="page">
  <nav class="site-nav">
    <a class="nav-home" href="#">HOME</a>
    <a class="nav-therapies" href="#">THERAPIES<span class="caret"></span></a>
    <a class="nav-approach" href="#">MY APPROACH</a>
    <a class="nav-resources" href="#">RESOURCES</a>
    <a class="nav-contact" href="#">CONTACT ME</a>
  </nav>

  <div class="brand"><span class="brand-dot"></span><span class="brand-name">BRIGHT PATH WELLNESS GROUP</span></div>

  <div class="illustration" role="img" aria-label="Illustration of a therapist with a tablet beside a client whose head is being completed with puzzle pieces, with a tangled-thought speech bubble and stacked puzzle pieces"></div>

  <p class="hero-kicker"><span>Reclaim Your Life</span> from Chronic Pain</p>
  <h1 class="hero-title">Pain Reprocessing<br>Therapy</h1>
  <p class="hero-acronym">(PRT)</p>

  <h2 class="section-title">What is PRT?</h2>
  <p class="intro-text">As a PRT therapist at Bright Path Wellness Group, I help people discover a fresh path out of pain. Pain Reprocessing Therapy (PRT) is grounded in neuroscience, showing us that chronic pain isn't just about the body, it's about how your brain interprets signals.</p>

  <svg class="connectors" width="1200" height="675" aria-hidden="true">
    <polyline points="100,487 269,487 376,378 471,378" fill="none" stroke="var(--line)" stroke-width="1"/>
    <polyline points="1125,210 893,210 837,270 768,270" fill="none" stroke="var(--line)" stroke-width="1"/>
  </svg>

  <h2 class="audience-heading">Who Is<strong>PRT For?</strong></h2>

  <div class="audience-item item-back">
    <span class="audience-icon"><svg width="18" height="18" viewBox="0 0 18 18"><path d="M9 2v14M5 6l4-4 4 4" fill="none" stroke="var(--navy)" stroke-width="1.6" stroke-linecap="round"/></svg></span>
    <div class="audience-copy"><h3>Chronic back, neck,<br>or joint pain</h3><p>lingering pain limits your life<br>despite clear scans or<br>endless therapies, PRT can<br>offer a new approach.</p></div>
  </div>
  <div class="audience-item item-fibro">
    <span class="audience-icon"><svg width="18" height="18" viewBox="0 0 18 18"><circle cx="9" cy="9" r="3" fill="none" stroke="var(--navy)" stroke-width="1.6"/><path d="M9 1v3M9 14v3M1 9h3M14 9h3" stroke="var(--navy)" stroke-width="1.6" stroke-linecap="round"/></svg></span>
    <div class="audience-copy"><h3>Fibromyalgia and<br>widespread pain</h3><p>Pain reprocessing therapy for<br>fibromyalgia addresses both<br>physical and emotional<br>aspects, providing real hope.</p></div>
  </div>
  <div class="audience-item item-headache">
    <span class="audience-icon"><svg width="18" height="18" viewBox="0 0 18 18"><path d="M10 2L6 10h4l-2 6" fill="none" stroke="var(--navy)" stroke-width="1.6" stroke-linejoin="round" stroke-linecap="round"/></svg></span>
    <div class="audience-copy"><h3>Migraines or tension<br>headaches</h3><p>For those who are tired of<br>masking symptoms and want<br>to improve wellbeing.</p></div>
  </div>
  <div class="audience-item item-ibs">
    <span class="audience-icon"><svg width="18" height="18" viewBox="0 0 18 18"><circle cx="9" cy="9" r="6" fill="none" stroke="var(--navy)" stroke-width="1.6"/><circle cx="9" cy="9" r="2" fill="var(--navy)"/></svg></span>
    <div class="audience-copy"><h3>IBS, pelvic pain, or<br>nerve-type aches</h3><p>If you experience discomfort<br>where traditional methods<br>haven't helped, PRT explores<br>the mind-body connection<br>for relief.</p></div>
  </div>
</div>
</body>
</html>
```